Insurance Agency Flyer

Create a flyer that encompasses the basic services that our agency offers. Flyer wording, logo, and company font are attached. See our website at www.tavenmork.com for additional details.

Target Market(s)

Prospective clients

Industry/Entity Type

Insurance Agency

Other font styles liked:
• baker signet com

```html
<!DOCTYPE html>
<html lang="en">
<head>
<meta charset="utf-8">
<title>The Tavenmork Company – Insurance Flyer</title>
<link href="https://fonts.googleapis.com/css2?family=EB+Garamond:wght@400;500;600&display=swap" rel="stylesheet">
<style>
  :root {
    --red: #e0173a;
    --charcoal: #4d4d4f;
    --slate: #6b6b6d;
    --row: #ececec;
    --ink: #2b2b2b;
    --paper: #ffffff;
  }
  * { box-sizing: border-box; margin: 0; padding: 0; }
  html, body { width: 800px; height: 1200px; overflow: hidden; background: var(--paper); }
  body { font-family: "EB Garamond", Georgia, serif; color: var(--ink); position: relative; }

  .hero {
    position: absolute; left: 0; top: 0; width: 800px; height: 428px;
    background: linear-gradient(180deg, #2e4a78 0%, #6e83a6 28%, #d9dde3 62%, #f1f1f1 100%);
  }
  .hero-rule { position: absolute; left: 0; top: 408px; width: 800px; height: 40px; }

  .tag {
    position: absolute; height: 30px; background: var(--slate); color: #fff;
    font-size: 13px; letter-spacing: .4px; text-transform: uppercase;
    padding: 7px 10px 0; white-space: nowrap;
  }
  .tag::after {
    content: ""; position: absolute; left: 0; bottom: -8px;
    border-top: 8px solid #333; border-left: 8px solid transparent;
  }

  .copy { position: absolute; font-size: 12.5px; line-height: 16px; }

  .cov-title {
    position: absolute; color: var(--red); font-size: 13.5px;
    text-transform: uppercase; text-decoration: underline; letter-spacing: .3px;
  }
  .cov-table { position: absolute; font-size: 12.5px; }
  .cov-row { display: flex; height: 22px; align-items: center; padding-left: 14px; }
  .cov-row:nth-child(odd) { background: var(--row); }
  .cov-row span { flex: 1; }

  .agency-copy {
    position: absolute; left: 36px; top: 893px; width: 730px;
    font-size: 11px; line-height: 15px; font-variant: small-caps; text-align: justify;
  }

  .brand { position: absolute; left: 100px; top: 1030px; display: flex; align-items: center; gap: 10px; }
  .brand-dot { width: 22px; height: 22px; border-radius: 50%; background: var(--red); }
  .brand-name { font-size: 30px; font-weight: 600; color: var(--red); }

  .contact-bar {
    position: absolute; left: 0; top: 1128px; width: 404px; height: 40px;
    background: var(--red); color: #fff; font-size: 11px;
    display: flex; align-items: center; gap: 22px; padding-left: 38px;
  }
  .contact-item { display: flex; align-items: center; gap: 6px; }
  .contact-item svg { width: 12px; height: 12px; fill: #fff; }

  .testimonial {
    position: absolute; left: 404px; top: 1010px; width: 396px; height: 190px;
    background: var(--charcoal); color: #fff; font-size: 12.5px; line-height: 16.5px;
    padding: 18px 24px 0 20px; text-align: justify;
  }
  .testimonial cite { display: block; font-style: normal; margin-top: 4px; }
</style>
</head>
<body>

<div class="hero" role="img" aria-label="Photo of cupped hands sheltering a model house, a family of figurines and a small car"></div>
<svg class="hero-rule" viewBox="0 0 800 40" preserveAspectRatio="none" aria-hidden="true">
  <path d="M0 20 Q400 8 800 16 L800 40 L0 40 Z" fill="#fff"/>
  <path d="M0 20 Q400 8 800 16" stroke="var(--red)" stroke-width="5" fill="none"/>
</svg>

<div class="tag" style="left:34px;top:452px;">About us</div>
<p class="copy" style="left:36px;top:498px;width:360px;">Established in 2008, The Tavenmork Company was created on the premise that both business and individual consumers should expect more from their insurance agency and agents. The Tavenmork Company is a full-service insurance agency that specializes in tailored insurance protection, risk management, and claims consultation.</p>

<div class="tag" style="left:400px;top:452px;">A professional agency with exceptional service</div>
<p class="copy" style="left:404px;top:498px;width:360px;">The Tavenmork Company is a firm of proven professionals who are dedicated to caring and conscientious service. We are committed to a high standard of excellence in all that we do and strive to establish a firm relationship of mutual trust and service with each of our clients.</p>

<div class="tag" style="left:34px;top:606px;width:310px;">We offer complete insurance services</div>

<div class="cov-title" style="left:36px;top:668px;">Personal coverages</div>
<div class="cov-table" style="left:36px;top:700px;width:352px;">
  <div class="cov-row"><span>Homeowners</span><span>Valuable Property</span></div>
  <div class="cov-row"><span>Automobile</span><span>Life</span></div>
  <div class="cov-row"><span>Renters / Condo</span><span>Disability</span></div>
  <div class="cov-row"><span>Personal umbrella</span><span>Health</span></div>
</div>

<div class="cov-title" style="left:404px;top:668px;">Business coverages</div>
<div class="cov-table" style="left:404px;top:700px;width:362px;">
  <div class="cov-row"><span>Commercial General Liability</span><span>Commercial Excess Liability</span></div>
  <div class="cov-row"><span>Commercial Property</span><span>Professional Liability</span></div>
  <div class="cov-row"><span>Workers' Compensation</span><span>Employment Practices Liability</span></div>
  <div class="cov-row"><span>Business Automobile</span><span>Life</span></div>
  <div class="cov-row"><span></span><span>Health</span></div>
</div>

<div class="tag" style="left:34px;top:826px;width:362px;">We are an independent trusted circle agency</div>
<p class="agency-copy">Being an Independent Trusted Circle Agency means that we take our time to make sure that we learn about your needs, and that each policy is built to specifically meet those needs. We are committed to treating you as a person, not another policy number. We will work with you to identify the insurance products and services that are right for you, your family, and/or your business. We accomplish this by using our expertise and multiple insurance carrier relationships to customize your insurance program. We will explain the different coverage and options available to you, and should the need arise, we will be there to guide you through the claims process. Our promise to you is that we will return your phone calls and emails promptly and respond to your requests in a timely manner. Also, we work diligently to stay informed about the latest insurance trends to understand how they might affect our clients.</p>

<div class="brand">
  <span class="brand-dot"></span>
  <span class="brand-name">Tavenmork</span>
</div>

<div class="contact-bar">
  <span class="contact-item">
    <svg viewBox="0 0 12 12" aria-hidden="true"><circle cx="6" cy="6" r="6"/></svg>
    www.tavenmork.com
  </span>
  <span class="contact-item">
    <svg viewBox="0 0 12 12" aria-hidden="true"><path d="M2 1l2 0 1 3-1.4 1a7 7 0 0 0 3.4 3.4L8 7l3 1v2a1 1 0 0 1-1 1A9 9 0 0 1 1 2a1 1 0 0 1 1-1z"/></svg>
    555.214.0371
  </span>
  <span class="contact-item">
    <svg viewBox="0 0 12 12" aria-hidden="true"><path d="M6 0a4 4 0 0 1 4 4c0 3-4 8-4 8S2 7 2 4a4 4 0 0 1 4-4zm0 2.5a1.5 1.5 0 1 0 0 3 1.5 1.5 0 0 0 0-3z"/></svg>
    <span style="line-height:12px;">4827 Harlow Ave.<br>Dunmore, SC 29999</span>
  </span>
</div>

<blockquote class="testimonial">
  “ The Tavenmork Company has consistently responded to the needs of our business, finding us well priced policies.” The Tavenmork Company has consistently responded to the needs of our business, finding us well priced policies without sacrificing coverage. They always respond to our needs quickly and effectively, provide great consultation, are knowledgeable, and care greatly about our business and success.”
  <cite>Martin Alder ( long time client)</cite>
</blockquote>

</body>
</html>
```